Global Weight loss program

we need a business card based in Brooklyn , NY called PeppertonRUN . Mara Dulvik Tenbrook the founder and creator of PeppertonRUN Movement. A business based around nutrition, health, Whole Foods and fitness.

Industry/Entity Type

Food Service

Contact Information for Business Card

Phone number : 718-555-0143
website www.peppertonrun.com
email : mara@peppertonrun.com

Font styles to use
Sans Serif

Requirements
Must have
• logo colors
• green black and gold
Nice to have
• must be simple and sharp.
Should not have
• pictures of items

```html
<!DOCTYPE html>
<html lang="en">
<head>
<meta charset="utf-8">
<title>PeppertonRUN Business Card</title>
<link href="https://fonts.googleapis.com/css2?family=Open+Sans:wght@400;600;700&display=swap" rel="stylesheet">
<style>
  :root {
    --stage: #2a2a2a;
    --green: #76b82a;
    --green-dark: #5e9e1f;
    --green-light: #8cc63f;
    --gold: #c9a13b;
    --gold-light: #e2c067;
    --ink: #2b2b2b;
    --paper: #f7f7f5;
    --faint: #e3ead9;
    --white: #ffffff;
  }
  * { box-sizing: border-box; margin: 0; padding: 0; }
  html, body { width: 1200px; height: 800px; overflow: hidden; }
  body {
    background: var(--stage);
    font-family: "Open Sans", Arial, sans-serif;
    position: relative;
  }
  .card {
    position: absolute;
    left: 340px;
    width: 520px;
    height: 297px;
    border-radius: 2px;
    overflow: hidden;
    box-shadow: 0 10px 30px rgba(0,0,0,.45);
  }
  .card-front {
    top: 70px;
    background: radial-gradient(circle at 55% 40%, var(--green-light), var(--green) 55%, var(--green-dark));
    display: flex;
    flex-direction: column;
    align-items: center;
    justify-content: center;
  }
  .card-back { top: 430px; background: var(--paper); }

  .brand { display: flex; align-items: center; gap: 12px; }
  .brand-mark { width: 30px; height: 30px; background: var(--gold); }
  .brand-name { font-weight: 700; letter-spacing: .5px; white-space: nowrap; }
  .card-front .brand-mark { background: var(--gold-light); }
  .card-front .brand-name { color: var(--white); font-size: 40px; }
  .tagline {
    font-size: 11px;
    letter-spacing: 3px;
    margin-top: 4px;
    white-space: nowrap;
  }
  .card-front .tagline { color: rgba(255,255,255,.85); }

  .back-brand {
    position: absolute;
    left: 36px;
    top: 112px;
    width: 240px;
  }
  .card-back .brand { gap: 10px; }
  .card-back .brand-mark { width: 22px; height: 22px; }
  .card-back .brand-name { color: var(--ink); font-size: 26px; }
  .card-back .tagline { color: #9a9a9a; font-size: 9px; letter-spacing: 2px; }

  .divider {
    position: absolute;
    left: 292px;
    top: 70px;
    width: 2px;
    height: 140px;
    background: linear-gradient(var(--gold), var(--green) 60%, rgba(118,184,42,0));
  }
  .figure-placeholder {
    position: absolute;
    right: 36px;
    top: 14px;
    width: 110px;
    height: 280px;
    border-radius: 50px 50px 10px 10px;
    background: linear-gradient(var(--faint), rgba(227,234,217,.3));
  }
  .contact { position: absolute; left: 310px; top: 70px; }
  .person-name { color: var(--green); font-weight: 700; font-size: 17px; white-space: nowrap; }
  .person-title { color: var(--gold); font-weight: 600; font-size: 10px; margin: 2px 0 22px 12px; }
  .contact-list { list-style: none; }
  .contact-list li {
    display: flex;
    align-items: center;
    gap: 8px;
    font-size: 11px;
    color: var(--ink);
    margin-bottom: 8px;
  }
  .contact-list svg { width: 11px; height: 11px; fill: none; stroke: var(--green); stroke-width: 2; }
</style>
</head>
<body>
  <section class="card card-front" aria-label="Card front">
    <div class="brand">
      <span class="brand-mark"></span>
      <span class="brand-name">PeppertonRUN</span>
    </div>
    <p class="tagline">Fitness, Nutrition and Health</p>
  </section>

  <section class="card card-back" aria-label="Card back">
    <div class="figure-placeholder" role="img" aria-label="Faint silhouette of a fitness figure"></div>
    <div class="back-brand">
      <div class="brand">
        <span class="brand-mark"></span>
        <span class="brand-name">PeppertonRUN</span>
      </div>
      <p class="tagline">Fitness, Nutrition and Health</p>
    </div>
    <div class="divider"></div>
    <div class="contact">
      <p class="person-name">Mara Dulvik Tenbrook</p>
      <p class="person-title">Founder</p>
      <ul class="contact-list">
        <li><svg viewBox="0 0 12 12"><path d="M3 1 L5 3 L4 5 Q5 7 7 8 L9 7 L11 9 L9 11 Q2 10 1 3 Z"/></svg>718-555-0143</li>
        <li><svg viewBox="0 0 12 12"><rect x="1" y="3" width="10" height="7"/><path d="M1 3 L6 7 L11 3"/></svg>mara@peppertonrun.com</li>
        <li><svg viewBox="0 0 12 12"><circle cx="6" cy="6" r="5"/><path d="M1 6 H11 M6 1 Q3 6 6 11 Q9 6 6 1"/></svg>www.peppertonrun.com</li>
      </ul>
    </div>
  </section>
</body>
</html>
```